Medical Billing - Professional Marketing Flier

We are needing help designing a clean and professional looking easy to read marketing flier for a medical billing practice. The text needs to be large enough to print. We are looking for a 5.5 x 8.5 design that we can edit the text as needed. I have included our logo and what we initially want it to say. Please keep in mind, we also want our logo and contact details on the flier. Let me know if you have any questions.

```html
<!DOCTYPE html>
<html lang="en">
<head>
<meta charset="utf-8">
<title>Vega Claims Partners – Flier</title>
<link rel="stylesheet" href="https://fonts.googleapis.com/css2?family=Crimson+Pro:wght@700&family=Montserrat:wght@500;600&family=Oswald:wght@600&display=swap">
<style>
  :root {
    --stage: #d9d9d9;
    --paper: #ffffff;
    --ink: #1b1b1b;
    --pink: #e2679a;
    --violet: #6b4fa8;
    --brand: #8a55a8;
    --blue-light: #0a97d6;
    --blue-deep: #0560ae;
    --navy: #0b4784;
    --night: #050608;
    --hex: #bfe3f5;
    --dots: #c67fb5;
  }
  * { margin: 0; padding: 0; box-sizing: border-box; }
  html, body { width: 1200px; height: 1117px; overflow: hidden; }
  body { background: var(--stage); font-family: "Montserrat", sans-serif; }

  .flier {
    position: absolute; left: 260px; top: 32px;
    width: 680px; height: 1052px;
    background: var(--paper);
    overflow: hidden;
  }

  .hex-pattern {
    position: absolute; left: 0; top: 0; width: 130px; height: 460px;
    background: linear-gradient(160deg, rgba(191,227,245,.55), rgba(191,227,245,0) 80%);
  }
  .hex-pattern--lower {
    left: auto; right: 0; top: 570px; width: 70px; height: 225px;
    background: linear-gradient(200deg, rgba(191,227,245,.6), rgba(191,227,245,0) 85%);
  }
  .dot-pattern {
    position: absolute; right: 8px; top: 10px; width: 100px; height: 190px;
    background: radial-gradient(ellipse at 80% 45%, rgba(198,127,181,.55), rgba(198,127,181,0) 70%);
  }

  .brand {
    position: absolute; left: 0; right: 0; top: 130px;
    text-align: center;
  }
  .brand__name {
    font-family: "Montserrat", sans-serif; font-weight: 600;
    font-size: 50px; letter-spacing: 2px; color: var(--brand);
    line-height: 1;
  }

  .service { position: absolute; left: 0; right: 0; text-align: center; }
  .section-head {
    position: relative; height: 31px; margin: 0 auto; width: 534px;
  }
  .section-head::before {
    content: ""; position: absolute; left: 0; right: 0; top: 14px; height: 3px;
    background: linear-gradient(90deg, var(--pink), var(--violet));
  }
  .section-head__label {
    position: relative; display: inline-block;
    width: 172px; height: 31px; line-height: 31px; border-radius: 4px;
    background: linear-gradient(90deg, var(--pink), var(--violet));
    color: #fff; font-family: "Crimson Pro", serif; font-weight: 700; font-size: 22px;
  }
  .service__text {
    width: 560px; margin: 16px auto 0;
    font-size: 13.4px; line-height: 15.6px; color: var(--ink); font-weight: 500;
  }

  .contact-band {
    position: absolute; left: 0; top: 797px; width: 680px; height: 160px;
    background: linear-gradient(90deg, var(--blue-light), var(--blue-deep));
    text-align: center; color: #fff;
  }
  .contact-band__label {
    display: inline-block; margin-top: 22px;
    width: 172px; height: 31px; line-height: 31px; border-radius: 4px;
    background: var(--navy);
    font-family: "Crimson Pro", serif; font-weight: 700; font-size: 22px;
  }
  .contact-band__text {
    width: 550px; margin: 15px auto 0;
    font-size: 13.4px; line-height: 15.6px; font-weight: 500;
  }

  .contact-bar {
    position: absolute; left: 0; top: 957px; width: 680px; height: 95px;
    background: var(--night); color: #fff;
    display: flex; align-items: center;
  }
  .contact-bar__phone {
    display: flex; align-items: center; margin-left: 58px;
    font-family: "Oswald", sans-serif; font-weight: 600; font-size: 42px; letter-spacing: -.5px;
  }
  .contact-bar__phone svg { margin-right: 10px; }
  .contact-bar__divider { width: 2px; height: 52px; background: #fff; margin: 0 20px; }
  .contact-bar__links { list-style: none; font-size: 17px; font-weight: 600; line-height: 24px; }
  .contact-bar__links li { display: flex; align-items: center; }
  .contact-bar__links .dot {
    width: 13px; height: 13px; border-radius: 50%; background: var(--dots); margin-right: 8px;
  }
</style>
</head>
<body>
<main class="flier">
  <div class="hex-pattern" role="img" aria-label="Faint blue hexagon network decoration"></div>
  <div class="hex-pattern hex-pattern--lower" role="img" aria-label="Faint blue hexagon network decoration"></div>
  <div class="dot-pattern" role="img" aria-label="Pink halftone dot pattern"></div>

  <header class="brand">
    <h1 class="brand__name">Vega Claims Partners</h1>
  </header>

  <section class="service" style="top:312px">
    <h2 class="section-head"><span class="section-head__label">Medical Billing</span></h2>
    <p class="service__text">Would you prefer to spend time focusing on your clients and running your practice rather than trying to stay up to speed with the constantly changing medical billing rules and regulations? Let us help you by managing your medical billing and dealing with the insurance companies on your behalf! We work with you to tailor the entire medical billing process to suit your practices needs while making it as smooth and painless as possible.</p>
  </section>

  <section class="service" style="top:481px">
    <h2 class="section-head"><span class="section-head__label">Aging</span></h2>
    <p class="service__text">Are you leaving money on the table? Are you able to do the follow-through needed to keep your aging in check and more money flowing into your practice? Are you uncertain about how to get insurance to pay on claims that should be covered but for some reason they decided not to? We can clean up your aging, reduce the amount of time it takes for claims to pay out, and we can keep your aging to a minimum.</p>
  </section>

  <section class="service" style="top:648px">
    <h2 class="section-head"><span class="section-head__label">Credentialing</span></h2>
    <p class="service__text">Are you wanting to get contracted with insurance companies but aren’t sure how to go about it? Are you wanting to expand your client base by having the option to bill insurance? Let us take the confusion out of what can seem like a daunting task! We can get you and your practitioners contracted with the insurance companies of your choice and help you navigate through the process every step of the way!</p>
  </section>

  <section class="contact-band">
    <h2 class="contact-band__label">Contact Us</h2>
    <p class="contact-band__text">If any of these processes are something you would like our help with or to consult with us on, please email us or give us a call! We specialize in billing and contracting for Nutritionists and Dietitians. We would love to help you expand your business and take the pain and frustration out of billing so you can focus on your clients.</p>
  </section>

  <footer class="contact-bar">
    <div class="contact-bar__phone">
      <svg width="22" height="40" viewBox="0 0 22 40" aria-hidden="true">
        <defs><linearGradient id="phoneTone" x1="0" y1="0" x2="0" y2="1"><stop offset="0" stop-color="#e2679a"/><stop offset="1" stop-color="#8a55a8"/></linearGradient></defs>
        <path d="M9 2 L13 10 L9 14 C8 20 9 25 12 29 L17 27 L21 35 L15 39 C5 34 1 20 4 5 Z" fill="url(#phoneTone)"/>
      </svg>
      555-014-2288
    </div>
    <div class="contact-bar__divider"></div>
    <ul class="contact-bar__links">
      <li><span class="dot"></span>admin@vegaclaimspartners.com</li>
      <li><span class="dot"></span>www.vegaclaimspartners.com</li>
    </ul>
  </footer>
</main>
</body>
</html>
```